Talcott Land Surveyors Business Card

We are a land surveying company looking for a business card with a clean, sharp design. We would like for our design to portray our logo on one side, and contact information on the other w/ or w/o logo. Our colors preferred are navy blue, grey/silver, white and black. thank you!

Industry/Entity Type

Surveyor

Contact Information for Business Card

Talcott Land Surveyors
Gordon Pavlikova, P.L.S.
(781) 555-0193
Talcottlandsurveyors@mailbox.example
Talcottlandsurveyors.example
287 Willowmere Lane, Reading MA 01999

Requirements
Must have
• 1. Company Name
2. Personal name and title
3. phone number
4. email.
5. website
6. address

```html
<!DOCTYPE html>
<html lang="en">
<head>
<meta charset="utf-8">
<title>Talcott Land Surveyors – Business Card</title>
<link href="https://fonts.googleapis.com/css2?family=Lato:wght@400;700;900&display=swap" rel="stylesheet">
<style>
  :root {
    --navy: #2e3592;
    --navy-dark: #262c7e;
    --silver: #7b7b7d;
    --white: #ffffff;
    --backdrop: #9b9b9b;
    --ink-grey: #6a6a6a;
  }
  * { margin: 0; padding: 0; box-sizing: border-box; }
  html, body {
    width: 1200px; height: 900px; overflow: hidden;
    background: var(--backdrop);
    font-family: "Lato", Arial, sans-serif;
  }
  .stage { position: relative; width: 1200px; height: 900px; }

  .card {
    position: absolute;
    left: 285px;
    width: 630px; height: 360px;
    border-radius: 26px;
    overflow: hidden;
    box-shadow: 0 6px 18px rgba(0,0,0,0.25);
  }

  /* Back side */
  .card-back { top: 60px; background: var(--navy); }
  .back-pattern {
    position: absolute; inset: 0;
    background: linear-gradient(160deg, var(--navy) 0%, var(--navy-dark) 100%);
  }
  .back-brand {
    position: absolute; right: 70px; top: 160px;
    display: flex; align-items: center; gap: 10px;
    color: var(--white);
    font-weight: 700; font-size: 15px; letter-spacing: 0.5px;
  }
  .brand-dot {
    width: 22px; height: 22px; border-radius: 50%;
    background: var(--white);
  }

  /* Front side */
  .card-front { top: 480px; background: var(--white); }
  .front-waves { position: absolute; inset: 0; }
  .front-brand {
    position: absolute; right: 40px; top: 62px;
    display: flex; align-items: center; gap: 12px;
    color: var(--navy);
    font-weight: 900; font-size: 21px; letter-spacing: 1px;
    text-transform: uppercase; line-height: 1.15;
  }
  .front-brand .brand-dot { background: var(--navy); width: 34px; height: 34px; }
  .holder {
    position: absolute; left: 52px; top: 160px;
  }
  .holder-name {
    color: var(--navy); font-weight: 900; font-size: 26px;
  }
  .holder-title {
    color: var(--ink-grey); font-size: 17px; margin-top: 2px;
  }
  .contact {
    position: absolute; left: 300px; top: 248px;
    color: var(--white); font-size: 14px; line-height: 1.45;
  }
  .contact-address { margin-bottom: 4px; }
  .contact-row { display: flex; align-items: center; gap: 10px; }
  .contact-row svg { width: 14px; height: 14px; flex: none; }
</style>
</head>
<body>
<main class="stage">

  <section class="card card-back" aria-label="Card back">
    <div class="back-pattern" role="img" aria-label="Faint repeating surveyor-tripod pattern across navy background"></div>
    <div class="back-brand"><span class="brand-dot"></span>Talcott Land Surveyors</div>
  </section>

  <section class="card card-front" aria-label="Card front">
    <svg class="front-waves" viewBox="0 0 630 360" preserveAspectRatio="none" aria-hidden="true">
      <path d="M95 360 C165 250 300 212 412 214 C300 224 198 258 122 360 Z" fill="var(--silver)"/>
      <path d="M135 360 C205 262 330 228 430 226 C545 224 605 165 630 95 L630 360 Z" fill="var(--navy)"/>
    </svg>

    <div class="front-brand"><span class="brand-dot"></span><span>Talcott<br>Land Surveyors</span></div>

    <div class="holder">
      <div class="holder-name">Gordon Pavlikova, P.L.S.</div>
      <div class="holder-title">Founder &amp; CEO</div>
    </div>

    <div class="contact">
      <div class="contact-address">287 Willowmere Lane,<br>Reading MA 01999</div>
      <div class="contact-row">
        <svg viewBox="0 0 24 24" fill="var(--white)"><path d="M6.6 10.8a15 15 0 0 0 6.6 6.6l2.2-2.2a1 1 0 0 1 1-.25 11.4 11.4 0 0 0 3.6.57 1 1 0 0 1 1 1V20a1 1 0 0 1-1 1A17 17 0 0 1 3 4a1 1 0 0 1 1-1h3.5a1 1 0 0 1 1 1c0 1.25.2 2.450.57 3.57a1 1 0 0 1-.25 1z"/></svg>
        <span>(781) 555-0193</span>
      </div>
      <div class="contact-row">
        <svg viewBox="0 0 24 24" fill="none" stroke="var(--white)" stroke-width="2"><rect x="2" y="5" width="20" height="14" rx="1"/><path d="M2 6l10 7 10-7"/></svg>
        <span>Talcottlandsurveyors@mailbox.example</span>
      </div>
      <div class="contact-row">
        <svg viewBox="0 0 24 24" fill="none" stroke="var(--white)" stroke-width="2"><circle cx="12" cy="12" r="10"/><path d="M2 12h20M12 2c3 3 3 17 0 20M12 2c-3 3-3 17 0 20"/></svg>
        <span>www.talcottlandsurveyors.example</span>
      </div>
    </div>
  </section>

</main>
</body>
</html>
```